Graphic Design for a Info Card

We would like a graphic design for an info card . We would like the colours to correspond to our logo , you can add in the colours navy blue or yellow if you would like. We would like it to have the following information. We want something that really pops. We would like the size to be 4 1/2 x 6 .

ATTENTION!! Delivery Promo! Order from us on the @hopplemeals app or @marlinrunner app on FRIDAYS and receive a FREE Sample of our one of our meal prep meals in your bag!
DID YOU KNOW?! Meal Prep is another great service that we offer. Saving you time, promoting your health, and best of all providing a delicious lunch . You can find more info on our website www.brivoranpantry.example . All orders are available for delivery or pickup!

```html
<!DOCTYPE html>
<html lang="en">
<head>
<meta charset="utf-8">
<title>Brivoran Pantry – Delivery Promo Card</title>
<link rel="stylesheet" href="https://fonts.googleapis.com/css2?family=Montserrat:wght@500;600;700;800;900&family=Mali:wght@700&display=swap">
<style>
  :root {
    --lime: #95c11f;
    --lime-pale: #e6f0cf;
    --leaf: #3c8a1e;
    --leaf-soft: #5a9e2c;
    --ink: #2b2b2b;
    --grey: #9a9a9a;
    --logo-grey: #8c8c8c;
    --white: #ffffff;
    --navy: #0b1499;
    --yellow: #f4ec1e;
    --stage: #f1f1f1;
    --scooter-red: #d8141c;
    --phone-teal: #5fd3b8;
  }
  * { box-sizing: border-box; margin: 0; padding: 0; }
  html, body { width: 960px; height: 1200px; overflow: hidden; background: var(--stage); }
  .card {
    position: absolute; left: 30px; top: 0;
    width: 900px; height: 1200px;
    background: var(--white);
    overflow: hidden;
    font-family: "Montserrat", sans-serif;
    color: var(--ink);
  }
  .card-shapes { position: absolute; inset: 0; }
  .brand {
    position: absolute; top: 40px; left: 0; width: 100%;
    display: flex; justify-content: center; align-items: center; gap: 10px;
  }
  .brand-dot { width: 14px; height: 14px; border-radius: 50%; background: var(--lime); }
  .brand-name {
    font-weight: 800; font-size: 36px; letter-spacing: 1px;
    color: var(--logo-grey); text-transform: uppercase;
  }
  .headline {
    position: absolute; top: 168px; left: 94px; width: 751px;
    text-align: center;
    font-weight: 900; font-size: 74px; letter-spacing: 1px;
    color: var(--white); line-height: 86px;
  }
  .promo-title {
    position: absolute; top: 296px; left: 0; width: 100%;
    text-align: center;
    font-family: "Mali", cursive;
    font-weight: 700; font-size: 60px; color: var(--grey);
    line-height: 76px;
  }
  .promo-copy {
    position: absolute; top: 380px; left: 40px; width: 820px;
    text-align: center;
    font-weight: 500; font-size: 24.5px; letter-spacing: 1.4px;
    line-height: 34px; color: var(--ink);
  }
  .promo-copy .hl { color: var(--lime); font-weight: 800; }
  .did-you-know {
    position: absolute; top: 818px; left: 484px;
    font-weight: 800; font-size: 37px; letter-spacing: 1.5px;
    color: var(--white); line-height: 48px;
  }
  .service-copy {
    position: absolute; top: 873px; left: 489px; width: 410px;
    font-weight: 500; font-size: 21.5px; letter-spacing: 1px;
    line-height: 26.7px; color: #111;
  }
  .service-copy .web {
    font-weight: 800; color: var(--white); letter-spacing: 1.2px;
  }
  .availability {
    position: absolute; left: 471px; top: 1069px;
    width: 410px; height: 66px;
    background: var(--navy);
    padding: 8px 0 0 32px;
    font-weight: 800; font-size: 21.5px; letter-spacing: 1.2px;
    line-height: 26px; color: var(--yellow);
  }
</style>
</head>
<body>
  <main class="card">
    <svg class="card-shapes" width="900" height="1200" viewBox="0 0 900 1200" xmlns="http://www.w3.org/2000/svg">
      <defs>
        <linearGradient id="meal-fill" x1="0" y1="0" x2="0" y2="1">
          <stop offset="0" stop-color="#7fae3a"/>
          <stop offset="1" stop-color="#a4714a"/>
        </linearGradient>
        <linearGradient id="scene-fill" x1="0" y1="0" x2="1" y2="1">
          <stop offset="0" stop-color="var(--phone-teal)"/>
          <stop offset="1" stop-color="var(--scooter-red)"/>
        </linearGradient>
        <linearGradient id="leaf-fill" x1="0" y1="0" x2="0" y2="1">
          <stop offset="0" stop-color="var(--leaf-soft)"/>
          <stop offset="1" stop-color="var(--leaf)"/>
        </linearGradient>
      </defs>

      <!-- green lower field -->
      <polygon class="green-field" points="900,470 900,1200 0,1200 0,905 420,760" fill="var(--lime)"/>

      <!-- rule lines and pale bands -->
      <polygon class="pale-band" points="420,118 870,118 900,153 450,153" fill="var(--lime-pale)"/>
      <polygon class="pale-band" points="0,152 150,152 180,186 0,186" fill="var(--lime-pale)"/>
      <polygon class="pale-band" points="300,272 720,272 740,288 310,288" fill="var(--lime-pale)"/>
      <rect class="rule" x="233" y="113" width="423" height="3" fill="var(--lime)"/>
      <rect class="rule" x="0" y="127" width="427" height="3" fill="var(--lime)"/>
      <rect class="rule" x="157" y="290" width="279" height="3" fill="var(--lime)"/>
      <rect class="rule" x="696" y="287" width="186" height="3" fill="var(--lime)"/>

      <!-- headline banner -->
      <polygon class="headline-banner" points="94,150 751,150 845,272 186,272" fill="var(--lime)"/>

      <!-- leaf illustration areas -->
      <rect role="img" aria-label="Decorative green leaf illustration" x="37" y="172" width="72" height="136" rx="10" fill="url(#leaf-fill)"/>
      <rect role="img" aria-label="Decorative green leaf illustration" x="833" y="320" width="48" height="90" rx="8" fill="url(#leaf-fill)"/>

      <!-- meal prep photos -->
      <rect role="img" aria-label="Photo of meal prep container with chicken, egg, rice and vegetables" x="454" y="528" width="189" height="267" rx="22" fill="url(#meal-fill)"/>
      <rect role="img" aria-label="Photo of meal prep container with chicken, egg, rice and broccoli" x="654" y="528" width="188" height="267" rx="22" fill="url(#meal-fill)"/>

      <!-- delivery illustration -->
      <rect role="img" aria-label="Illustration of a smartphone with map and location pin beside a red delivery scooter" x="30" y="607" width="410" height="541" rx="30" fill="url(#scene-fill)" opacity="0.85"/>
    </svg>

    <div class="brand">
      <span class="brand-dot"></span>
      <span class="brand-name">Brivoran Pantry</span>
    </div>

    <h1 class="headline">ATTENTION!!</h1>

    <h2 class="promo-title">Delivery Promo!</h2>

    <p class="promo-copy">
      Order from us on the <span class="hl">@hopplemeals</span> app or<br>
      <span class="hl">@marlinrunner</span> app on <span class="hl">FRIDAYS</span> and receive<br>
      a <span class="hl">FREE</span> Sample of our one of our meal prep<br>
      meals in your bag!
    </p>

    <h3 class="did-you-know">DID YOU KNOW?!</h3>

    <p class="service-copy">
      Meal Prep is another great<br>
      service that we offer. Saving<br>
      you time, promoting your<br>
      health, and best of all providing<br>
      a delicious lunch . You can find<br>
      more info on our website<br>
      <span class="web">www.brivoranpantry.example</span>
    </p>

    <p class="availability">
      ALL ORDERS ARE AVAILABLE<br>
      FOR DELIVERY OR PICKUP!
    </p>
  </main>
</body>
</html>
```